VFX Company Business Card Design Project

The Pixel Harbor is a decentralized Visual Effects Studio servicing the television and feature film industries.
Project Brief:
Take our logo that was previously designed on Sketch Forum and make a double sided business card.
Requirements:
- Card MUST be double sided.
- Front of card MUST have the yellow part of our logo against the dark grey background.
- Back of card is completely up to the designer.
- Back of card must include the complete company logo.
Please follow these File Preparation guidelines:
http://printmarlow.example/infopage?file=filetype_en&s=PrintMarlow_new&lang=en
Industry/Entity Type
Business
Look and feel
Each slider illustrates characteristics of the customer's brand and the style your logo design should communicate.

```html
<!DOCTYPE html>
<html lang="en">
<head>
<meta charset="utf-8">
<title>The Pixel Harbor – Business Card Presentation</title>
<link rel="stylesheet" href="https://fonts.googleapis.com/css2?family=Jost:ital,wght@0,300;0,400;0,600;1,600&display=swap">
<style>
  :root {
    --board-light: #d9a97e;
    --board-dark: #c58f62;
    --label: #1c1c1c;
    --card: #2e2e2e;
    --brand-yellow: #fcc52c;
    --brand-grey: #6b7577;
    --text-light: #f2f2f2;
    --band-light: #eef3e4;
    --band-grey: #5f6a6c;
    --band-text-dark: #3a3a3a;
  }
  * { margin: 0; padding: 0; box-sizing: border-box; }
  html, body { width: 1200px; height: 788px; overflow: hidden; }
  body { font-family: "Jost", sans-serif; }
  .board {
    position: relative; width: 1200px; height: 788px;
    background: radial-gradient(ellipse at 50% 45%, var(--board-light), var(--board-dark));
  }
  .label {
    position: absolute; font-size: 22px; font-weight: 400; color: var(--label);
    transform: translateX(-50%);
  }
  .label--back { left: 600px; top: 32px; }
  .label--front1 { left: 327px; top: 403px; }
  .label--front2 { left: 900px; top: 403px; }
  .card {
    position: absolute; width: 524px; height: 299px; border-radius: 22px;
    background: var(--card); overflow: hidden;
    box-shadow: 0 4px 10px rgba(0,0,0,0.45);
    color: var(--text-light);
  }
  .card--back { left: 338px; top: 78px; }
  .card--front1 { left: 54px; top: 446px; }
  .card--front2 { left: 623px; top: 446px; }
  .wordmark { position: absolute; left: 0; right: 0; text-align: center; font-weight: 600; }
  .card--back .wordmark { top: 40px; font-size: 40px; color: var(--brand-grey); }
  .card--front1 .wordmark { top: 110px; font-size: 50px; color: var(--brand-yellow); }
  .card--front2 .wordmark { top: 120px; font-size: 40px; color: var(--brand-grey); display: flex; justify-content: center; align-items: center; gap: 18px; }
  .wordmark__dot { width: 34px; height: 34px; border-radius: 50%; background: var(--brand-yellow); display: inline-block; }
  .person { position: absolute; top: 138px; left: 0; right: 0; text-align: center; font-weight: 300; font-size: 20px; }
  .person__role { font-size: 14px; font-weight: 400; }
  .contact { position: absolute; left: 0; right: 0; text-align: center; font-size: 13px; font-weight: 400; }
  .contact--phones { top: 176px; }
  .contact--address { top: 196px; }
  .contact strong { font-weight: 600; font-style: italic; }
  .bands { position: absolute; left: 0; top: 0; }
  .band-text { position: absolute; font-size: 14px; }
  .band-text--web { left: 24px; top: 235px; color: var(--band-text-dark); }
  .band-text--mail { right: 28px; top: 253px; color: var(--text-light); }
  .site { position: absolute; left: 0; right: 0; top: 256px; text-align: center; font-size: 20px; letter-spacing: 4px; font-weight: 400; }
</style>
</head>
<body>
<main class="board" role="img" aria-label="Warm tan damask wallpaper backdrop">
  <span class="label label--back">Back</span>
  <span class="label label--front1">Front - 1</span>
  <span class="label label--front2">Front - 2</span>

  <section class="card card--back">
    <div class="wordmark">The Pixel Harbor</div>
    <p class="person">Your Name, <span class="person__role">Designation</span></p>
    <p class="contact contact--phones"><strong>phone</strong> 123-456-7890 &nbsp;|&nbsp; <strong>cell</strong> 123-456-7890</p>
    <p class="contact contact--address">0000#, Area Name, Street Name, State Name, Country code</p>
    <svg class="bands" width="524" height="299" viewBox="0 0 524 299">
      <polygon points="242,245 524,245 524,280 222,280" fill="var(--band-grey)"/>
      <polygon points="0,227 307,227 280,262 0,262" fill="var(--band-light)"/>
    </svg>
    <span class="band-text band-text--web">www.pixelharbor.example</span>
    <span class="band-text band-text--mail">info@pixelharbor.example</span>
  </section>

  <section class="card card--front1">
    <div class="wordmark">The Pixel Harbor</div>
    <p class="site">www.pixelharbor.example</p>
  </section>

  <section class="card card--front2">
    <div class="wordmark"><span class="wordmark__dot"></span>The Pixel Harbor</div>
    <p class="site">www.pixelharbor.example</p>
  </section>
</main>
</body>
</html>
```